Book cover: Stormy Days Survival for Kids (A5)

I have a book called Stormy Days Survival for Teens. It is a book for teenagers which gives them tips and tactics on how to survive life's challenges regarding friends, family, feelings, relationships and hard stuff in life generally. I will upload the cover of this book but you can see it on my past jobs as one of the designers her eon Pixel Bazaar did it for me.
I have a new book I've written called Stormy Days Survival for Kids. This is a parallel book to Stormy Days Survival for Teens, but it is specifically for 8 to 12 or 13 year olds, rather than for older teens.
A very important aspect of this job is that it SHOULD MATCH in some strong way - the Stormy Days Survival for Teens book. I will be selling them together, displaying them together and I want them to look like two of a pair. It might be that you use the same image as the first book but change the colour of the image so that it is bright orange and green perhaps? Or that there is another image but in the image is placed in the exact same position across the book as the first book. It needs to look like the books are by the same author.
However, I would like this one to look a bit "younger", more kid friendly. For example, a font that looks like it is for kids, or kids' writing perhaps.
I dont want to have photos on the book, and I dont think I want cartoons or drawings - because I'm not sure how this will tie in with the first book.
I want it to look modern, fresh and designed specifically for kids. The text needs to be:
Stormy Days Survival - For Kids!
Tips and ideas for 8 to 13 year olds about how to stay cool, calm and confident on even the toughest days!
The back cover is going to mostly just have the table of contents listed and a blurb, with one or two cartoons which I will supply. I am keen to pick a designer to just do the front cover first and will ask them to do the back cover later.
UPDATED: I have attached three files with fonts that I like.

```html
<!DOCTYPE html>
<html lang="en">
<head>
<meta charset="utf-8">
<title>Stormy Days Survival – For Kids! Front Cover</title>
<link rel="stylesheet" href="https://fonts.googleapis.com/css2?family=Bebas+Neue&family=Kalam:wght@700&family=Open+Sans:wght@400;600&display=swap">
<style>
  :root {
    --page-bg: #eeeeee;
    --cover-bg: #ffffff;
    --title-orange: #f7941d;
    --title-blue: #29a8e0;
    --ink: #1a1a1a;
    --tile-pink: #f4a6a0;
    --tile-yellow: #fbe98a;
    --tile-blue: #8fd3ef;
    --tile-red: #ea6a5e;
  }
  * { box-sizing: border-box; margin: 0; padding: 0; }
  html, body {
    width: 1200px;
    height: 1000px;
    overflow: hidden;
    background: var(--page-bg);
  }
  .cover {
    position: absolute;
    left: 282px;
    top: 50px;
    width: 636px;
    height: 900px;
    background: var(--cover-bg);
    overflow: hidden;
    box-shadow: 0 4px 18px rgba(0,0,0,0.12);
  }
  .tile-field {
    position: absolute;
    inset: 0;
    width: 636px;
    height: 900px;
  }
  .title {
    position: absolute;
    left: 62px;
    top: 200px;
    font-family: "Bebas Neue", "Arial Narrow", sans-serif;
    font-weight: 400;
    line-height: 0.9;
    letter-spacing: 1px;
  }
  .title-line { display: block; font-size: 118px; }
  .title-line--orange { color: var(--title-orange); }
  .title-line--blue { color: var(--title-blue); }
  .subtitle {
    position: absolute;
    left: 150px;
    top: 575px;
    width: 450px;
    font-family: "Open Sans", Arial, sans-serif;
    font-size: 20px;
    line-height: 1.35;
    color: var(--ink);
    text-align: center;
  }
  .credits {
    position: absolute;
    right: 36px;
    top: 770px;
    text-align: left;
    font-family: "Open Sans", Arial, sans-serif;
    color: var(--ink);
  }
  .author-name {
    font-family: "Kalam", "Comic Sans MS", cursive;
    font-weight: 700;
    font-size: 30px;
    color: var(--title-orange);
    line-height: 1.1;
  }
  .author-role { font-size: 17px; font-weight: 600; margin-top: 2px; }
  .illustrator { font-size: 11px; margin-top: 2px; }
</style>
</head>
<body>
  <main class="cover">
    <svg class="tile-field" viewBox="0 0 636 900" aria-hidden="false">
      <defs>
        <linearGradient id="tilesTop" x1="0" y1="0" x2="1" y2="1">
          <stop offset="0" stop-color="var(--tile-yellow)"/>
          <stop offset="0.35" stop-color="var(--tile-pink)"/>
          <stop offset="0.65" stop-color="var(--tile-blue)"/>
          <stop offset="1" stop-color="var(--tile-yellow)"/>
        </linearGradient>
        <linearGradient id="tilesBottom" x1="0" y1="0" x2="1" y2="1">
          <stop offset="0" stop-color="var(--tile-yellow)"/>
          <stop offset="0.4" stop-color="var(--tile-pink)"/>
          <stop offset="0.7" stop-color="var(--tile-red)"/>
          <stop offset="1" stop-color="var(--tile-blue)"/>
        </linearGradient>
      </defs>
      <path class="tile-cluster tile-cluster--top" role="img"
            aria-label="Cluster of overlapping translucent coloured squares in pink, yellow, red and blue"
            d="M150 0 H636 V430 C600 440 560 400 520 360 C430 270 330 180 250 110 C200 70 160 30 150 0 Z"
            fill="url(#tilesTop)" opacity="0.55"/>
      <path class="tile-cluster tile-cluster--bottom" role="img"
            aria-label="Cluster of overlapping translucent coloured squares in pink, yellow, red and blue"
            d="M0 660 C60 640 130 650 190 690 C280 750 380 820 450 900 H0 Z"
            fill="url(#tilesBottom)" opacity="0.55"/>
    </svg>

    <h1 class="title">
      <span class="title-line title-line--orange">Stormy Days</span>
      <span class="title-line title-line--orange">Survival</span>
      <span class="title-line title-line--blue">For Kids!</span>
    </h1>

    <p class="subtitle">Tips and ideas for 8 to 13 year olds about how to stay cool, calm and confident on even the toughest days!</p>

    <div class="credits">
      <p class="author-name">Maren Tolliver</p>
      <p class="author-role">Clinical psychologist</p>
      <p class="illustrator">Illustrated by: Rafael D. Moura</p>
    </div>
  </main>
</body>
</html>
```